A new novel about the early days of The Marlows needs a book cover design

The title of the book is A LANTERN IN WINTER
The cover should also include "a novel" and "by Tom Holloway" Those can be together or separate.
The design element I'd like to incorporate is the iconic "Dock Wall" photo of The Marlows in 1960, which I've attached below. Since we're not sure if we can get the rights to the actual photo, it's probably best if the design merely references that photo, or distorts it in an interesting way. But it should be very clear that the book is about the Marlows.
The novel is in many ways based on that photo and evokes the city of Hamburg in 1960, which was gritty, raw, and sexually charged (as were The Marlows).
The tone of the novel is romantic, passionate, and very funny - but never broad and silly.

```html
<!DOCTYPE html>
<html lang="en">
<head>
<meta charset="utf-8">
<title>A Lantern in Winter — Book Cover</title>
<link rel="stylesheet" href="https://fonts.googleapis.com/css2?family=League+Gothic&family=Gelasio:ital@1&display=swap">
<style>
  :root {
    --page: #ffffff;
    --ink: #000000;
    --stripe: #4a4a4b;
    --title: #ffdd00;
    --dash: #ffffff;
    --byline: #ffffff;
    --photo-dark: #141414;
    --photo-mid: #3a3a3a;
  }
  html, body {
    margin: 0;
    padding: 0;
    width: 1200px;
    height: 1000px;
    overflow: hidden;
    background: var(--page);
  }
  .canvas {
    position: relative;
    width: 1200px;
    height: 1000px;
  }
  .cover {
    position: absolute;
    left: 347px;
    top: 95px;
    width: 505px;
    height: 809px;
    overflow: hidden;
    background: var(--ink);
  }
  .cover__stripes {
    position: absolute;
    inset: 0;
    width: 100%;
    height: 100%;
  }
  .cover__photo {
    position: absolute;
    left: 0;
    top: 228px;
    width: 100%;
    height: 352px;
    background:
      radial-gradient(ellipse at 70% 40%, rgba(110,110,110,0.35), transparent 60%),
      linear-gradient(180deg, var(--photo-mid) 0%, var(--photo-dark) 55%, #2c2c2c 100%);
  }
  .cover__dashes {
    position: absolute;
    left: 116px;
    display: flex;
    gap: 24px;
  }
  .cover__dashes--top { top: 59px; }
  .cover__dashes--bottom { top: 710px; }
  .cover__dash {
    width: 36px;
    height: 11px;
    background: var(--dash);
  }
  .cover__title {
    position: absolute;
    left: 0;
    right: 0;
    top: 118px;
    margin: 0;
    padding-left: 6px;
    text-align: center;
    font-family: "League Gothic", "Oswald", sans-serif;
    font-weight: 400;
    font-size: 142px;
    line-height: 0.93;
    letter-spacing: 1px;
    color: var(--title);
    text-transform: uppercase;
  }
  .cover__title span { display: block; }
  .cover__byline {
    position: absolute;
    left: 0;
    right: 0;
    top: 762px;
    margin: 0;
    text-align: center;
    font-family: "Gelasio", "Georgia", serif;
    font-style: italic;
    font-size: 17px;
    color: var(--byline);
  }
</style>
</head>
<body>
  <main class="canvas">
    <section class="cover">
      <svg class="cover__stripes" viewBox="0 0 505 809" aria-hidden="true">
        <defs>
          <pattern id="diagonal-stripes" patternUnits="userSpaceOnUse" width="204" height="809" x="-22" patternTransform="rotate(-25)">
            <rect x="0" y="0" width="102" height="809" fill="var(--stripe)"/>
          </pattern>
        </defs>
        <rect width="505" height="809" fill="url(#diagonal-stripes)"/>
      </svg>

      <div class="cover__photo" role="img" aria-label="Black-and-white 1960 photograph of The Marlows posing with guitars and a snare drum in front of the Dock Wall in Hamburg"></div>

      <div class="cover__dashes cover__dashes--top" aria-hidden="true">
        <span class="cover__dash"></span><span class="cover__dash"></span><span class="cover__dash"></span><span class="cover__dash"></span><span class="cover__dash"></span>
      </div>

      <h1 class="cover__title">
        <span>A</span>
        <span>Lantern</span>
        <span>In</span>
        <span>Winter</span>
      </h1>

      <div class="cover__dashes cover__dashes--bottom" aria-hidden="true">
        <span class="cover__dash"></span><span class="cover__dash"></span><span class="cover__dash"></span><span class="cover__dash"></span><span class="cover__dash"></span>
      </div>

      <p class="cover__byline">A novel by Tom Holloway</p>
    </section>
  </main>
</body>
</html>
```